Innovation Presentation Template

I need a unique template design for a presentation on Innovation used exclusively inside of our company. I'd prefer to work in Apple Keynote but can take a .ppt and convert it. The template should appeal to a broad audience of diverse job descriptions. This is a one-time presentation that will last between 30 and 45 minutes. The design should provide a strong visual appeal with multiple chart layouts to support highlighted test points (no bullets, I hate bullets), graphics, line art, and video/photos. My presentations are sparse, never more that 2 concepts per chart (usually one). Our company is a high tech manufacturer selling products in many markets ranging from Government to consumer. The final design should include style a style guide including suggested fonts, colors, graph formats, suggested word art, etc.

Target Market(s)

The audience is internal employees only. Strong corporate branding is not required in this presentation.

Industry/Entity Type

Government

Colors
3277b5
faa54b

Requirements
Must have
• Strong visual appeal helping to support the communication of simple concepts (that have been broken down from complex subject matter).

Multiple chart template forms to support different forms of communication including text points, data charts, graphics, photos, and videos.

Visuals will be memorable, but not overpower the content. Visuals will help convey the content.

Well conceived and coordinated color pallets. Fonts guides (that I can access).

You can visit our company web site at www.KOVEX.com to see logo and corporate look/feel. It would be good to build logo into a few of the chart templates, but not all.
Nice to have
• Keynote (please). I can live with .ppt if I have to.

Many charts will make a point with simple single sentences. Find a way to make the sentences graphically interesting by varying font and/or color of specific words to help drive points.

Note that colors that I've identified below are based upon the blue used in our logo and the orange that complements it. I'm not married to these but use them as guidelines.
Should not have
• Noise. Corporate nauseia.

```html
<!DOCTYPE html>
<html lang="en">
<head>
<meta charset="utf-8">
<title>Project Title Here</title>
<link href="https://fonts.googleapis.com/css2?family=Saira+Semi+Condensed:wght@400;500;700&display=swap" rel="stylesheet">
<style>
  :root {
    --brand-blue: #034f97;
    --brand-orange: #f68b1f;
    --body-bg: #f1f5fb;
    --text-dark: #2a2e33;
    --white: #ffffff;
    --photo-dark: #3d3d3d;
    --photo-light: #9a9a9a;
  }
  * { margin: 0; padding: 0; box-sizing: border-box; }
  html, body { width: 1200px; height: 900px; overflow: hidden; background: var(--white); }
  body { font-family: "Saira Semi Condensed", "Arial Narrow", sans-serif; }
  .slide { position: relative; width: 1200px; height: 900px; }

  .header { position: absolute; top: 0; left: 0; width: 1200px; height: 138px; background: var(--white); }
  .header-accent { position: absolute; left: 0; top: 27px; width: 14px; height: 70px; background: var(--brand-orange); }
  .project-title { position: absolute; left: 27px; top: 24px; font-size: 60px; font-weight: 400; line-height: 76px; color: var(--brand-blue); letter-spacing: 0.5px; }
  .project-title .highlight { color: var(--brand-orange); }

  .hero-photo { position: absolute; left: 0; top: 138px; width: 1200px; height: 327px;
    background: linear-gradient(100deg, var(--photo-dark) 0%, #5a5a5a 35%, var(--photo-light) 60%, #6e6e6e 100%); }

  .title-band { position: absolute; left: 0; top: 468px; width: 1200px; height: 63px; background: var(--brand-blue); border-top: 0; }
  .band-rule { position: absolute; left: 0; top: 465px; width: 1200px; height: 3px; background: var(--white); }
  .band-notch { position: absolute; left: 66px; top: 444px; }
  .slide-title { position: absolute; left: 27px; top: 0; line-height: 63px; font-size: 37px; font-weight: 500; color: var(--white); }

  .content { position: absolute; left: 0; top: 531px; width: 1200px; height: 275px; background: var(--body-bg); }
  .column { position: absolute; top: 26px; width: 530px; font-size: 22px; line-height: 30px; color: var(--text-dark); text-align: justify; }
  .column p + p { margin-top: 30px; }
  .column-left { left: 27px; }
  .column-right { left: 633px; }

  .footer-rule { position: absolute; left: 0; top: 806px; width: 1200px; height: 4px; background: var(--brand-orange); }
  .footer { position: absolute; left: 0; top: 810px; width: 1200px; height: 90px; background: var(--brand-blue); }
  .company-name { position: absolute; left: 18px; top: 0; line-height: 90px; font-size: 44px; font-weight: 700; color: var(--white); letter-spacing: 1px; }
  .page-number { position: absolute; right: 24px; top: 0; line-height: 90px; font-size: 30px; font-weight: 700; color: var(--white); }
</style>
</head>
<body>
<div class="slide">
  <header class="header">
    <div class="header-accent"></div>
    <h1 class="project-title"><span class="highlight">PROJECT</span> TITLE HERE</h1>
  </header>

  <div class="hero-photo" role="img" aria-label="Blurred black and white photo of an open office with desks and an office chair"></div>

  <div class="band-rule"></div>
  <svg class="band-notch" width="48" height="26" viewBox="0 0 48 26" aria-hidden="true">
    <polygon points="0,26 24,0 48,26" fill="#034f97"/>
  </svg>
  <section class="title-band">
    <h2 class="slide-title">Slide Title Here</h2>
  </section>

  <section class="content">
    <div class="column column-left">
      <p>Lorem ipsum dolor sit Lorem ipsum dolor sit Lorem ipsum dolor sit Lorem ipsum dolor sit Lorem ipsum dolor sit Lorem ipsum dolor sit Lorem ipsum dolor sit.</p>
      <p>Lorem ipsum dolor sit Lorem ipsum dolor sit Lorem ipsum dolor sit Lorem ipsum</p>
    </div>
    <div class="column column-right">
      <p>Lorem ipsum dolor sit Lorem ipsum dolor sit Lorem ipsum dolor sit Lorem ipsum dolor sit Lorem ipsum dolor sit Lorem ipsum dolor sit Lorem ipsum dolor sit.</p>
      <p>Lorem ipsum dolor sit Lorem ipsum dolor sit Lorem ipsum dolor sit Lorem ipsum</p>
    </div>
  </section>

  <div class="footer-rule"></div>
  <footer class="footer">
    <span class="company-name">KOVEX</span>
    <span class="page-number">1</span>
  </footer>
</div>
</body>
</html>
```